BLUE HAVEN (Business Card for Training Company)

Blue Haven is a training and consultancy company with a focus on executive protection and medical. I would like the card to be nice and sharp, not overdone and in black and red. I would also like it to highlight that it is "A Dravin Company"

I would like it to be simple and highlight a few things.

1. Name
2. Title
3. Phone Number
4. Email

I would also like www.dravinholdings.example/blue-haven to be on the card somewhere.

Target Market(s)

Security Companies

Industry/Entity Type

Security

Contact Information for Business Card

Blue Haven is a training and consultancy company with a focus on executive protection and medical. I would like the card to be nice and sharp, not overdone and in black and red. I would also like it to highlight that it is "A Dravin Company" I would like it to be simple and highlight a few things. 1. Name 2. Title 3. Phone Number 4. Email I would also like www.dravinholdings.example/blue-haven to be on the card somewhere.

Requirements
Must have
• A Dravin Company listed on the card and the website
Nice to have
• Highlight Medical Training, Consultancy & Executive Protection Courses

```html
<!DOCTYPE html>
<html lang="en">
<head>
<meta charset="utf-8">
<title>Blue Haven — Business Card</title>
<link rel="stylesheet" href="https://fonts.googleapis.com/css2?family=Roboto:ital,wght@0,300;0,400;0,700;0,900;1,400&display=swap">
<style>
  :root {
    --bg: #e6e6e6;
    --card: #ffffff;
    --red: #6b1111;
    --ink: #151515;
    --soft-ink: #2a2a2a;
  }
  * { box-sizing: border-box; margin: 0; padding: 0; }
  html, body { width: 1200px; height: 900px; overflow: hidden; }
  body {
    background: var(--bg);
    font-family: "Roboto", Arial, sans-serif;
    color: var(--ink);
    position: relative;
  }
  .card {
    position: absolute;
    left: 260px;
    width: 680px;
    height: 390px;
    background: var(--card);
    border-bottom: 6px solid var(--red);
    box-shadow: 0 4px 14px rgba(0,0,0,0.12);
    overflow: hidden;
  }
  .card--front { top: 40px; }
  .card--back { top: 470px; }

  /* Front */
  .brand {
    position: absolute;
    top: 110px;
    left: 0; right: 0;
    text-align: center;
  }
  .brand__name {
    display: inline-flex;
    align-items: center;
    gap: 14px;
    font-weight: 900;
    font-size: 58px;
    letter-spacing: 1px;
    color: var(--red);
    line-height: 1;
  }
  .brand__mark {
    width: 22px; height: 22px;
    background: var(--ink);
  }
  .brand__parent {
    margin-top: 16px;
    font-size: 15px;
    letter-spacing: 9px;
    color: var(--ink);
  }
  .front__note {
    position: absolute;
    bottom: 44px;
    left: 0; right: 0;
    text-align: center;
    font-style: italic;
    font-size: 17px;
    letter-spacing: 1.2px;
    color: var(--ink);
  }

  /* Back */
  .person {
    position: absolute;
    top: 148px;
    right: 396px;
    text-align: right;
    white-space: nowrap;
  }
  .person__name {
    font-weight: 900;
    font-size: 30px;
    color: var(--red);
    letter-spacing: 0.5px;
    line-height: 1.1;
  }
  .person__title {
    margin-top: 4px;
    font-weight: 300;
    font-size: 19px;
    color: var(--soft-ink);
  }
  .divider {
    position: absolute;
    left: 298px;
    top: 150px;
    width: 2px;
    height: 80px;
    background: var(--ink);
  }
  .contact {
    position: absolute;
    left: 318px;
    top: 152px;
    list-style: none;
  }
  .contact__item {
    display: flex;
    align-items: center;
    gap: 10px;
    height: 26px;
    font-size: 15.5px;
    letter-spacing: 0.5px;
    color: var(--soft-ink);
    white-space: nowrap;
  }
  .contact__icon { width: 15px; height: 15px; flex: none; }
  .services {
    position: absolute;
    left: 0; right: 0;
    bottom: 50px;
    text-align: center;
    font-size: 20px;
    letter-spacing: 1.3px;
    color: var(--soft-ink);
  }
</style>
</head>
<body>
  <section class="card card--front">
    <div class="brand">
      <div class="brand__name"><span class="brand__mark"></span>BLUE HAVEN</div>
      <div class="brand__parent">A DRAVIN COMPANY</div>
    </div>
    <p class="front__note">A Dravin Company listed on the card and the website</p>
  </section>

  <section class="card card--back">
    <div class="person">
      <h1 class="person__name">MARCUS HALE</h1>
      <p class="person__title">Founder &amp; CEO</p>
    </div>
    <div class="divider"></div>
    <ul class="contact">
      <li class="contact__item">
        <svg class="contact__icon" viewBox="0 0 16 16" fill="none" stroke="var(--red)" stroke-width="1.8"><rect x="4" y="1" width="8" height="14" rx="1.5"/><line x1="7" y1="12.5" x2="9" y2="12.5"/></svg>
        000 000 0000
      </li>
      <li class="contact__item">
        <svg class="contact__icon" viewBox="0 0 16 16" fill="none" stroke="var(--red)" stroke-width="1.8"><rect x="1" y="3" width="14" height="10" rx="1"/><polyline points="1.5,3.5 8,9 14.5,3.5"/></svg>
        info@bluehaven.example
      </li>
      <li class="contact__item">
        <svg class="contact__icon" viewBox="0 0 16 16" fill="none" stroke="var(--red)" stroke-width="1.8"><circle cx="9.5" cy="6.5" r="4.5"/><line x1="6.2" y1="9.8" x2="1.5" y2="14.5"/></svg>
        www.dravinholdings.example/blue-haven
      </li>
    </ul>
    <p class="services">Medical Training, Consultancy &amp; Executive Protection Courses</p>
  </section>
</body>
</html>
```